Vireo M.K. - Diagnostic Ultrasound Flyer

About US
Vireo M.K. is a concierge ultrasound company that provides onsite or offsite diagnostic ultrasounds. We have over 14 years experience in sonography, business management, and customer service. We offer both the physician and patient flexibility, convenience, and access to timely services.

We provide ultrasounds for the following specialties:
Obstetrics/Gynecology
Abdominal
Small Parts
Vascular

Company Features:
1. Onsite or Offsite Scans
2. Images Available Immediately for Referring Physician and Patient
3. Flexible Options for Ultrasound Interpretation/Billing
4. Access to Interpreting Radiologist
5. Final Report Process - 1-2 Business Days/ 1 hour for STAT.
6. PACS Storage with Secure Access.

We need a place to add in our contact information (address, email, website, phone)

We already have a logo and would like to use it ( they are attached). We would the colors to match the logo colors....maybe lighter version of yellow and blue.

```html
<!DOCTYPE html>
<html lang="en">
<head>
<meta charset="utf-8">
<title>Vireo M.K. – Diagnostic Ultrasound Flyer</title>
<link href="https://fonts.googleapis.com/css2?family=Poppins:ital,wght@0,500;0,600;0,700;0,800;1,800&family=Quicksand:wght@500;600&display=swap" rel="stylesheet">
<style>
  :root{
    --brand-blue:#1511a6;
    --brand-yellow:#fdb924;
    --text-grey:#454545;
    --paper:#ffffff;
    --photo-cool-1:#dfe8ec;
    --photo-cool-2:#b9c9d2;
    --photo-warm-1:#e9dfd6;
    --photo-warm-2:#c9b8a8;
  }
  *{margin:0;padding:0;box-sizing:border-box}
  html,body{width:960px;height:1200px;overflow:hidden;background:var(--paper)}
  .flyer{position:relative;width:960px;height:1200px;overflow:hidden;background:var(--paper);font-family:"Quicksand",sans-serif;color:var(--text-grey)}
  .flyer__art{position:absolute;inset:0}

  .brand{position:absolute;left:54px;top:38px;font-family:"Poppins",sans-serif;font-weight:800;font-size:56px;letter-spacing:1px;color:var(--brand-blue);line-height:1}

  .about{position:absolute;left:492px;top:486px;width:470px;text-align:center}
  .about__title{font-family:"Poppins",sans-serif;font-weight:700;font-size:25px;line-height:43px;color:var(--brand-blue);letter-spacing:.5px}
  .about__text{position:absolute;left:34px;top:64px;width:396px;font-size:20px;line-height:27.4px;font-weight:600;color:#fff;text-align:justify;text-align-last:center;hyphens:manual}

  .specialties{position:absolute;left:58px;top:712px}
  .specialties__title{font-family:"Poppins",sans-serif;font-style:italic;font-weight:800;font-size:21px;line-height:23px;color:var(--brand-blue)}
  .specialties__list{list-style:none;margin-top:10px}
  .specialties__item{display:flex;align-items:center;font-size:23.5px;font-weight:500;line-height:34.5px;color:var(--text-grey)}
  .tick{width:18px;height:18px;flex:none;margin:0 20px 0 8px}
  .tick--inline{margin:0 2px 0 8px}

  .features-bar{position:absolute;left:0;top:891px;width:537px;height:34px;background:var(--brand-blue);font-family:"Poppins",sans-serif;font-weight:600;font-size:18px;line-height:34px;color:var(--brand-yellow);padding-left:99px}
  .features{position:absolute;left:60px;top:936px;list-style:none}
  .features__item{display:flex;align-items:center;height:30px;font-size:19px;font-weight:500;color:var(--text-grey)}
  .features__num{width:17px;height:17px;border-radius:50%;background:var(--brand-blue);color:#fff;font-family:"Poppins",sans-serif;font-size:9px;font-weight:700;display:flex;align-items:center;justify-content:center;margin-right:16px;flex:none}

  .contact-bar{position:absolute;left:0;top:1124px;width:960px;height:48px;background:var(--brand-blue);font-family:"Poppins",sans-serif;font-weight:700;font-size:27px;line-height:48px;color:var(--brand-yellow);padding-left:76px;white-space:nowrap}
  .contact-bar span+span{margin-left:18px}
</style>
</head>
<body>
<main class="flyer">
  <svg class="flyer__art" width="960" height="1200" viewBox="0 0 960 1200">
    <defs>
      <linearGradient id="scan-photo-tone" x1="0" y1="0" x2="1" y2="1">
        <stop offset="0" stop-color="var(--photo-cool-1)"/>
        <stop offset=".55" stop-color="var(--photo-warm-1)"/>
        <stop offset="1" stop-color="var(--photo-warm-2)"/>
      </linearGradient>
      <linearGradient id="sonographer-photo-tone" x1="0" y1="0" x2="0" y2="1">
        <stop offset="0" stop-color="var(--photo-cool-1)"/>
        <stop offset=".6" stop-color="var(--photo-cool-2)"/>
        <stop offset="1" stop-color="#9fb3c4"/>
      </linearGradient>
      <clipPath id="scan-photo-shape">
        <circle cx="865" cy="590" r="605"/>
      </clipPath>
      <clipPath id="about-circle-shape">
        <circle cx="727" cy="662" r="235"/>
      </clipPath>
    </defs>

    <!-- top-right photo area -->
    <g clip-path="url(#scan-photo-shape)">
      <rect class="scan-photo" x="300" y="0" width="660" height="500" fill="url(#scan-photo-tone)" role="img" aria-label="Photo of a sonographer scanning a patient's leg with an ultrasound probe, monitor in the background"/>
    </g>
    <path d="M683,0 A605,605 0 0,0 431,174" fill="none" stroke="var(--brand-yellow)" stroke-width="9"/>

    <!-- circular sonographer photo -->
    <circle cx="290" cy="420" r="284" fill="url(#sonographer-photo-tone)" stroke="var(--brand-yellow)" stroke-width="9" role="img" aria-label="Photo of a smiling sonographer in a white coat holding an ultrasound probe"/>

    <!-- about us circle -->
    <circle cx="727" cy="662" r="235" fill="var(--brand-blue)"/>
    <g clip-path="url(#about-circle-shape)">
      <rect x="480" y="486" width="480" height="43" fill="var(--brand-yellow)"/>
    </g>
  </svg>

  <div class="brand">Vireo M.K.</div>

  <section class="about">
    <h2 class="about__title">ABOUT US</h2>
    <p class="about__text">Vireo M.K. is a concierge ultrasound company that provides onsite or offsite diagnostic ultrasounds. We have over 14 years experience in sonography, business manage&shy;ment, &amp; customer service. We offer both the physician &amp; patient flexi&shy;bility, convenience, &amp; access to timely services.</p>
  </section>

  <section class="specialties">
    <h3 class="specialties__title">We provide ultrasounds<br>for the following specialties</h3>
    <ul class="specialties__list">
      <li class="specialties__item"><svg class="tick" viewBox="0 0 20 20"><circle cx="10" cy="10" r="10" fill="var(--brand-yellow)"/><path d="M5.5 10.2l3 3 6-6.2" fill="none" stroke="#fff" stroke-width="2.2" stroke-linecap="round" stroke-linejoin="round"/></svg>Obstetrics/Gynecology</li>
      <li class="specialties__item"><svg class="tick" viewBox="0 0 20 20"><circle cx="10" cy="10" r="10" fill="var(--brand-yellow)"/><path d="M5.5 10.2l3 3 6-6.2" fill="none" stroke="#fff" stroke-width="2.2" stroke-linecap="round" stroke-linejoin="round"/></svg>Abdominal</li>
      <li class="specialties__item"><svg class="tick" viewBox="0 0 20 20"><circle cx="10" cy="10" r="10" fill="var(--brand-yellow)"/><path d="M5.5 10.2l3 3 6-6.2" fill="none" stroke="#fff" stroke-width="2.2" stroke-linecap="round" stroke-linejoin="round"/></svg>Small Parts<svg class="tick tick--inline" viewBox="0 0 20 20"><circle cx="10" cy="10" r="10" fill="var(--brand-yellow)"/><path d="M5.5 10.2l3 3 6-6.2" fill="none" stroke="#fff" stroke-width="2.2" stroke-linecap="round" stroke-linejoin="round"/></svg>Vascular</li>
    </ul>
  </section>

  <div class="features-bar">FEATURES</div>
  <ol class="features">
    <li class="features__item"><span class="features__num">1</span>Onsite or Offsite Scans</li>
    <li class="features__item"><span class="features__num">2</span>Images Available Immediately for Referring Physician and Patient</li>
    <li class="features__item"><span class="features__num">3</span>Flexible Options for Ultrasound Interpretation/Billing</li>
    <li class="features__item"><span class="features__num">4</span>Access to Interpreting Radiologist</li>
    <li class="features__item"><span class="features__num">5</span>Final Report Process - 1-2 Business Days/ 1 hour for STAT.</li>
    <li class="features__item"><span class="features__num">6</span>PACS Storage with Secure Access.</li>
  </ol>

  <footer class="contact-bar"><span>CALL US : 012-555-0147</span><span>WEB : WWW.VIREOMK.COM</span></footer>
</main>
</body>
</html>
```